House-share and Room Rental Website (With Focus on the Bedroom Landing Page)

Looking for website design for our House-share (executive accommodation) and room rental business.

Our company name is: Lodvenra could also be written as LodVenra or lodvenra. Either is fine .. just looking for a nice clean catchy logo to go with the design.

EXAMPLES
These are examples of other websites in this field that are doing well. this is a kind of baseline.
https://kelbrin.com.au/
https://www.tuvaplex.com/
https://www.nestorvi.com/
https://www.quillsa.net/
https://www.pendlebarrow.com.au/

Our business model is to rent rooms to people looking for high-quality accommodation. We fill the gap between those looking to rent rooms and those with rooms to rent. However, our model is slightly different from those already on the market as we looking to fill a massive gap in the market delivering upmarket rooms for rent.(Executive Accommodation) also in the back end will be coupled with a self management process in the back end.

We offer executive style accommodation that stands out above the rest. With special extras like fire safety.. and management processes that create happier homes. We are looking for a web design package that can help us grow and scale our business. We need a design that is captivating

Our MAIN focus is having a room landing page that stands out from the rest... The core of our business will rely on the promotion of the rooms in a share house... so the whole design relies on the BEDROOM landing page to drive results.

Target Market(s)

We have 2 markets we are aiming at ... the first market is people offering rooms to rent who want the highest rental return. The second market is people looking to rent safe, high-quality rooms, in houses that are well managed and looked after.

Industry/Entity Type

Share Economy

Logo Text

LodVenra

Number of Pages Required

5+ page

Font styles to use
Sans Serif

Colors
3276b5

Requirements
Must have
• A messaging system whereby we can create direct communication between those offering rooms and those looking for rooms.
• A call to action that says " Schedule an Inspection"
• Landing page for promoting rooms
• A home page for showing stock.
• Profile page for those selling rooms
• Profile page for those looking for rooms.
• A scheduling calendar for booking inspections
Nice to have
• Pages where new residents can lock in a room.. pay bond and rents.. and sign contracts
• Notifications
• SMS capabilities in the backend.
Should not have
• No script or handwriting fonts.

```html
<!DOCTYPE html>
<html lang="en">
<head>
<meta charset="utf-8">
<title>Lodvenra — Executive Rooms in Managed Share Houses</title>
<link rel="stylesheet" href="https://fonts.googleapis.com/css2?family=Raleway:wght@400;500;600;700&display=swap">
<style>
  :root {
    --brand-blue: #3276b5;
    --ink: #111111;
    --white: #ffffff;
    --band-grey: #5b5b5b;
    --footer-grey: #4e4e4e;
    --button-dark: #3a3f42;
    --soft-text: #e6e6e6;
  }
  * { box-sizing: border-box; margin: 0; padding: 0; }
  html, body { width: 1200px; height: 4380px; overflow: hidden; }
  body {
    position: relative;
    background: var(--white);
    font-family: "Raleway", Arial, sans-serif;
    color: var(--ink);
  }
  .photo { position: absolute; }

  /* Hero */
  .hero { position: absolute; left: 0; top: 0; width: 1200px; height: 628px; overflow: hidden; }
  .hero-photo {
    position: absolute; inset: 0;
    background:
      radial-gradient(ellipse at 50% 45%, rgba(120,130,135,.55) 0%, rgba(60,68,72,0) 55%),
      linear-gradient(180deg, #4a5356 0%, #3a4245 45%, #2b3133 100%);
  }
  .brand {
    position: absolute; left: 234px; top: 94px;
    display: flex; align-items: center; gap: 10px;
    color: var(--white); font-size: 28px; font-weight: 600; letter-spacing: .5px;
  }
  .brand-mark { width: 22px; height: 22px; background: var(--brand-blue); }
  .main-nav { position: absolute; left: 438px; top: 106px; display: flex; gap: 22px; }
  .main-nav a {
    color: var(--white); text-decoration: none;
    font-size: 19px; font-weight: 500; letter-spacing: .3px;
  }
  .hero-title {
    position: absolute; left: 0; width: 1200px; top: 270px;
    text-align: center; color: var(--white);
    font-size: 47px; font-weight: 500; line-height: 56px;
  }
  .search { position: absolute; left: 359px; top: 405px; display: flex; width: 517px; height: 38px; }
  .search-input {
    width: 362px; background: var(--brand-blue); color: var(--white);
    font-size: 14px; font-weight: 500; padding: 0 22px; line-height: 38px;
  }
  .search-button {
    flex: 1; background: var(--button-dark); color: var(--white);
    font-size: 17px; font-weight: 700; text-align: center; line-height: 38px;
  }

  .section-title {
    position: absolute; left: 0; width: 1200px; text-align: center;
    font-size: 46px; font-weight: 500;
  }

  /* Welcome */
  .welcome-text {
    position: absolute; left: 252px; width: 696px; top: 802px;
    text-align: center; font-size: 22.5px; line-height: 27.5px; font-weight: 500;
  }
  .amenity {
    position: absolute; top: 1005px; width: 160px; text-align: center;
    font-size: 10px; line-height: 12px; font-weight: 500; letter-spacing: .3px;
  }
  .amenity svg { display: block; margin: 0 auto 14px; }

  /* Featured room */
  .featured { position: absolute; left: 0; top: 1504px; width: 1200px; height: 622px; background: var(--band-grey); color: var(--white); }
  .featured .section-title { color: var(--white); top: 18px; }
  .featured-text {
    position: absolute; left: 234px; top: 90px; width: 352px;
    font-size: 17.5px; line-height: 27.5px; font-weight: 500; color: var(--soft-text);
  }
  .featured-footnote {
    position: absolute; left: 234px; top: 496px; width: 740px;
    font-size: 17.5px; line-height: 23.6px; font-weight: 500; color: var(--soft-text);
  }

  /* Call to action */
  .cta-button {
    position: absolute; left: 450px; top: 3533px; width: 300px; height: 42px;
    background: #0c0c0c; color: var(--white); text-align: center;
    line-height: 42px; font-size: 18px; font-weight: 500; letter-spacing: .3px;
  }

  /* Stats */
  .stats { position: absolute; left: 0; top: 3618px; width: 1200px; height: 310px; background: var(--band-grey); color: var(--white); }
  .stat { position: absolute; top: 66px; width: 200px; text-align: center; }
  .stat-number { font-size: 30px; font-weight: 500; }
  .stat-label { margin-top: 40px; font-size: 31px; font-weight: 500; line-height: 36px; }

  /* Safety */
  .safety-title { position: absolute; left: 0; width: 1200px; top: 3950px; text-align: center; font-size: 33px; font-weight: 500; }
  .safety-text {
    position: absolute; left: 258px; width: 684px; top: 4010px;
    text-align: center; font-size: 14.5px; line-height: 20.5px; font-weight: 500;
  }

  /* Footer */
  .site-footer { position: absolute; left: 0; top: 4193px; width: 1200px; height: 187px; background: var(--footer-grey); color: var(--white); }
  .social { position: absolute; left: 0; width: 1200px; top: 76px; display: flex; justify-content: center; gap: 38px; }
  .social span { width: 34px; height: 34px; border-radius: 50%; border: 3px solid var(--white); }
  .copyright { position: absolute; left: 0; width: 1200px; top: 136px; text-align: center; font-size: 12px; line-height: 17px; }
</style>
</head>
<body>

<header class="hero">
  <div class="hero-photo" role="img" aria-label="Photo of a white share house facade framed by palm trees, darkened"></div>
  <div class="brand"><span class="brand-mark"></span>Lodvenra</div>
  <nav class="main-nav">
    <a href="#">HOME</a><a href="#">ABOUT</a><a href="#">ROOMS</a><a href="#">GALLERY</a><a href="#">RESERVE</a><a href="#">CONTACT</a>
  </nav>
  <h1 class="hero-title">Best Place For<br>Find Your Room</h1>
  <div class="search">
    <div class="search-input">Looking For A Perfect Room ?</div>
    <div class="search-button">Search</div>
  </div>
</header>

<h2 class="section-title" style="top:738px">Welcome</h2>
<p class="welcome-text">Lodvenra offers executive rooms in share houses that are safe, well managed and looked after. We connect owners who want the best rental return with people who want a high-quality room, and we manage every home so residents live happier together.</p>

<div class="amenity" style="left:352px">
  <svg width="64" height="60" viewBox="0 0 64 60"><g fill="none" stroke="#111" stroke-width="4" stroke-linecap="round"><path d="M20 6v18M14 6v12a6 6 0 0 0 12 0V6M20 24v30"/><path d="M44 6c-6 4-6 18 0 22v26"/></g></svg>
  ELEGANT<br>RESTAURANT
</div>
<div class="amenity" style="left:527px">
  <svg width="72" height="60" viewBox="0 0 72 60"><g fill="none" stroke="#111" stroke-width="7" stroke-linecap="round"><path d="M6 22a42 42 0 0 1 60 0"/><path d="M16 33a28 28 0 0 1 40 0"/><path d="M26 44a14 14 0 0 1 20 0"/></g><circle cx="36" cy="53" r="5" fill="#111"/></svg>
  HIGH SPEED<br>INTERNET / WIFI
</div>
<div class="amenity" style="left:708px">
  <svg width="72" height="60" viewBox="0 0 72 60"><path d="M14 14h44l8 18v16h-8v6h-8v-6H22v6h-8v-6H6V32z" fill="#111"/><path d="M19 19h34l5 12H14z" fill="#fff"/><circle cx="16" cy="39" r="4" fill="#fff"/><circle cx="56" cy="39" r="4" fill="#fff"/></svg>
  CAR<br>PARKING
</div>

<div class="photo" style="left:234px;top:1133px;width:356px;height:239px;background:linear-gradient(135deg,#e9e4dc,#c9c4ba 60%,#8e9a98)" role="img" aria-label="Photo of a bright shared lounge with white chairs and shelving"></div>
<div class="photo" style="left:610px;top:1133px;width:356px;height:239px;background:linear-gradient(135deg,#9aa3a8,#d8d9d8 55%,#b7aea3)" role="img" aria-label="Photo of a made bed with navy and white pillows"></div>

<section class="featured">
  <h2 class="section-title">Special Room</h2>
  <p class="featured-text">Our featured room of the week is a bright executive bedroom with a queen bed, built-in wardrobe, a quiet study corner and its own heating and cooling. The house is fully furnished, cleaned every week and fitted with smoke alarms, fire blankets and a clear escape plan. Bills and fast wifi are included in the rent, and a house manager visits each month to keep things running smoothly.</p>
  <div class="photo" style="left:610px;top:163px;width:354px;height:249px;background:linear-gradient(135deg,#d9e4e6,#f0d4d8 50%,#c8d6dc)" role="img" aria-label="Photo of a pastel bedroom with colourful cushions"></div>
  <p class="featured-footnote">Like what you see? Book a time that suits you in our calendar and a house manager will meet you there to show you the room and the home.</p>
</section>

<h2 class="section-title" style="top:2239px">All Rooms</h2>
<div class="photo" style="left:234px;top:2318px;width:356px;height:307px;background:linear-gradient(160deg,#cfe3ec,#f1f1ef 55%,#8bbbd0)" role="img" aria-label="Photo of a bedroom with blue and white linen"></div>
<div class="photo" style="left:610px;top:2318px;width:356px;height:307px;background:linear-gradient(160deg,#c9c9c9,#2e3d55 45%,#e9e9e9)" role="img" aria-label="Photo of a bed with a navy headboard"></div>
<div class="photo" style="left:234px;top:2657px;width:732px;height:488px;background:linear-gradient(135deg,#f2f2f0,#dcdad5 55%,#b9b2a6)" role="img" aria-label="Photo of a white room with a writing desk and plants"></div>
<div class="photo" style="left:234px;top:3180px;width:356px;height:310px;background:linear-gradient(135deg,#f4ebe0,#e9c6b0 50%,#d88a7c)" role="img" aria-label="Photo of roses in a vase beside a bed"></div>
<div class="photo" style="left:610px;top:3180px;width:356px;height:310px;background:linear-gradient(135deg,#b9c9d3,#e3e6e6 50%,#2f4d63)" role="img" aria-label="Photo of a bedroom with windows and teal accents"></div>
<a class="cta-button" href="#">SCHEDULE AN INSPECTION</a>

<section class="stats">
  <div class="stat" style="left:198px"><div class="stat-number">300</div><div class="stat-label">Rooms</div></div>
  <div class="stat" style="left:510px"><div class="stat-number">100</div><div class="stat-label">Houses</div></div>
  <div class="stat" style="left:802px"><div class="stat-number">900</div><div class="stat-label">Happy<br>Residents</div></div>
</section>

<h2 class="safety-title">Safe, Well-Managed Homes</h2>
<p class="safety-text">"Every Lodvenra house is checked for fire safety, cleaned on a regular schedule and looked after by a dedicated house manager. Owners receive a strong rental return without the day-to-day work, while residents enjoy a quality room in a calm, friendly home. Message owners directly, compare rooms side by side, book an inspection in a few clicks, then lock in your room, pay your bond and sign your lease online."</p>

<footer class="site-footer">
  <div class="social"><span></span><span></span><span></span><span></span><span></span></div>
  <p class="copyright">copyright © 2018<br>All Right Reserved By Lodvenra</p>
</footer>

</body>
</html>
```